Larkspur Ridge Management - Business Cards

I need business cards. My current logo was designed by a designer at this site and I very much like and am happy with the results. I would like a business card that is trendy, unique, current yet professional. I deal with high net worth clients daily

Target Market(s)

Out of state investors looking to get into the rental market in Ohio

Industry/Entity Type

Property Management, Consulting

Contact Information for Business Card

Name, Title (Chief Financial Officer) office phone number (555) 817-3094 website address larkridgemgmt.example

Font styles to use
Sans Serif

Colors
0054AA
0677BA
7BADD7
CADEEF
E8F1F8
0094D4
00A9DD
6FCCEA
C7EBF8
E9F6FB
00AB8E
00BBA5
67D7C9
C6EFE9
E9F9F6

```html
<!DOCTYPE html>
<html lang="en">
<head>
<meta charset="utf-8">
<title>Larkspur Ridge Management – Business Cards</title>
<link href="https://fonts.googleapis.com/css2?family=Montserrat:wght@400;500;700;800&display=swap" rel="stylesheet">
<style>
  :root {
    --backdrop: #2b2b2c;
    --card-navy: #1c2b55;
    --accent-red: #d2272c;
    --paper-white: #ffffff;
    --shadow: rgba(0, 0, 0, 0.45);
  }
  * { margin: 0; padding: 0; box-sizing: border-box; }
  html, body {
    width: 1200px;
    height: 800px;
    overflow: hidden;
    background: var(--backdrop);
    font-family: "Montserrat", sans-serif;
  }
  .canvas {
    position: relative;
    width: 1200px;
    height: 800px;
  }
  .card {
    position: absolute;
    width: 525px;
    height: 300px;
    background: var(--card-navy);
    box-shadow: 0 18px 40px var(--shadow);
    overflow: hidden;
  }
  .card--brand { left: 600px; top: 90px; }
  .card--contact { left: 75px; top: 410px; }

  .stripe {
    position: absolute;
    height: 24px;
    background: linear-gradient(to bottom, var(--accent-red) 0 50%, var(--paper-white) 50% 100%);
  }
  .card--brand .stripe--left { left: 0; top: 96px; width: 165px; }
  .card--brand .stripe--right { right: 0; top: 180px; width: 120px; }
  .card--contact .stripe--right { right: 0; top: 105px; width: 175px; }
  .card--contact .stripe--left { left: 0; top: 222px; width: 120px; }

  .wordmark {
    position: absolute;
    color: var(--paper-white);
    font-weight: 800;
    text-transform: uppercase;
    line-height: 1.1;
    display: flex;
    align-items: center;
    gap: 10px;
  }
  .wordmark__square {
    width: 14px;
    height: 14px;
    background: var(--paper-white);
    flex: none;
  }
  .card--brand .wordmark {
    left: 195px;
    top: 112px;
    font-size: 19px;
    letter-spacing: 1px;
  }
  .card--contact .wordmark {
    left: 38px;
    top: 46px;
    font-size: 15px;
    letter-spacing: 1px;
  }

  .contact {
    position: absolute;
    left: 208px;
    top: 172px;
    color: var(--paper-white);
  }
  .contact__name {
    font-weight: 700;
    font-size: 15px;
    letter-spacing: 2.5px;
    text-transform: uppercase;
    margin-bottom: 8px;
  }
  .contact__line {
    font-weight: 400;
    font-size: 12px;
    letter-spacing: 2.4px;
    text-transform: uppercase;
    line-height: 1.6;
  }
</style>
</head>
<body>
  <main class="canvas">
    <section class="card card--brand" aria-label="Card front">
      <div class="stripe stripe--left"></div>
      <div class="stripe stripe--right"></div>
      <div class="wordmark">
        <span class="wordmark__square"></span>
        <span>Larkspur Ridge<br>Management</span>
      </div>
    </section>

    <section class="card card--contact" aria-label="Card back">
      <div class="wordmark">
        <span class="wordmark__square"></span>
        <span>Larkspur Ridge<br>Management</span>
      </div>
      <div class="stripe stripe--right"></div>
      <div class="stripe stripe--left"></div>
      <div class="contact">
        <p class="contact__name">Dana R. Whitfield</p>
        <p class="contact__line">Chief Financial Officer</p>
        <p class="contact__line">www.larkridgemgmt.example</p>
        <p class="contact__line">(555) 817-3094</p>
      </div>
    </section>
  </main>
</body>
</html>
```